Accounting & Tax Services in Edmonton, Canada-Needs Website Design & Improvement

I am starting my business for accounting and tax services in Canada. I have my website but not much happy with that. My services are for bookkeeping, accounting and tax services. We serve both individual and corporate clients. I am trying to bring new idea in the market for providing services at their facility or business. My existing website is www.qrmt.ca
Currently, this site is static but I want to improve it to dynamic or interactive in nature.

Target Market(s)

Edmonton and Surrounding Areas, Canada

Industry/Entity Type

Public Accounting

Logo Text

Harborline Ledger & Advisory Partners

Number of Pages Required

4 page

Font styles to use
Sans Serif

Colors

Designer to choose colors to be used in the design.

Requirements
Must have
• 4 Pages
• I a not sure what do we mean by coded and uncoded design. Need clarification
• Rest is explained in project description. It should have the ingredients to attract traffic in any professional website.
• Logo Design Text can be shortened, if required.
• Existing logo attached, just for reference.
Nice to have
• 5 Pages

```html
<!DOCTYPE html>
<html lang="en">
<head>
<meta charset="utf-8">
<title>Harborline Ledger &amp; Advisory Partners</title>
<link rel="stylesheet" href="https://fonts.googleapis.com/css2?family=Montserrat:wght@500;600;700&family=Mulish:wght@400;500;600;700&display=swap">
<style>
:root{
  --navy:#0f3f5c;
  --navy-deep:#0b3550;
  --teal:#4a94a6;
  --teal-dark:#1f5d7b;
  --slate:#8b9ca4;
  --ink:#2b2f33;
  --muted:#7a7f84;
  --link:#2d7fa3;
  --paper:#ffffff;
  --mist:#efefef;
  --line:#d9dde0;
}
*{box-sizing:border-box;margin:0;padding:0}
html,body{width:1200px;height:2835px;overflow:hidden}
body{font-family:"Mulish",Arial,sans-serif;color:var(--ink);background:var(--paper)}
.wrap{width:966px;margin:0 auto;position:relative}

/* hero */
.hero{position:relative;height:661px;overflow:hidden}
.hero-photo{position:absolute;inset:0;background:linear-gradient(135deg,#6f7a80 0%,#4b555c 40%,#39434a 70%,#2c353c 100%)}
.hero-shade{position:absolute;inset:0;background:rgba(20,30,38,.25)}
.topbar{position:relative;z-index:2;height:120px;display:flex;align-items:center;justify-content:space-between;border-bottom:1px solid rgba(255,255,255,.25)}
.brand{display:flex;align-items:center;gap:12px;color:#fff;font-family:"Mulish",sans-serif;font-weight:600;font-size:20px;line-height:1.2;width:300px}
.brand-mark{width:26px;height:26px;background:#fff;flex:none}
.nav{display:flex;gap:36px;list-style:none}
.nav a{color:#fff;text-decoration:none;font-size:16px;font-weight:500;letter-spacing:.3px}
.hero-copy{position:absolute;z-index:2;left:0;right:0;top:285px;text-align:center;color:#fff;font-family:"Montserrat",sans-serif}
.hero-title{font-size:48px;font-weight:600;letter-spacing:.5px}
.hero-sub{font-size:27px;font-weight:600;margin-top:4px;letter-spacing:.5px}
.arrow{position:absolute;z-index:2;top:322px}
.arrow.left{left:112px}.arrow.right{left:1066px}

/* services */
.services{height:486px;padding-top:56px}
.section-title{text-align:center;font-size:31px;font-weight:500;color:var(--ink)}
.rule{width:76px;height:2px;background:var(--ink);margin:14px auto 0}
.cards{display:flex;gap:22px;margin-top:26px}
.card{width:312px;height:308px;border:1px solid var(--line);box-shadow:0 1px 4px rgba(0,0,0,.06);text-align:center;padding-top:24px}
.card-icon{width:100px;height:100px;margin:0 auto}
.card h3{font-size:22px;font-weight:500;margin-top:36px;color:var(--ink)}
.card p{font-size:12px;color:var(--muted);line-height:1.6;margin:10px auto 0;width:230px}
.btn{display:inline-block;color:#fff;font-size:13px;font-weight:600;text-decoration:none;padding:11px 26px;letter-spacing:.3px}
.card .btn{margin-top:16px}
.btn.slate{background:var(--slate)}.btn.teal{background:var(--teal)}.btn.navy{background:var(--teal-dark)}

/* about */
.about{position:relative;height:446px;overflow:hidden}
.about-photo{position:absolute;inset:0;background:linear-gradient(120deg,#5f93a4 0%,#3b7f96 45%,#2f6f88 100%)}
.about-copy{position:relative;z-index:2;text-align:center;color:#fff;padding-top:94px}
.about-copy h2{font-size:33px;font-weight:500}
.about-copy .rule{background:#fff;margin-top:10px}
.about-copy p{width:760px;margin:26px auto 0;font-size:16px;line-height:1.55}
.btn.ghost{border:2px solid #fff;background:transparent;padding:14px 40px;margin-top:26px;font-size:14px}

/* why */
.why{height:471px;background:var(--mist)}
.why .wrap{display:flex;align-items:flex-start;padding-top:70px}
.why-text{width:390px;flex:none}
.why-text h2{font-size:34px;font-weight:500;color:var(--ink)}
.why-text p{font-size:15px;color:var(--muted);line-height:1.65;margin-top:18px;padding-left:6px;width:384px}
.why-text p + p{margin-top:12px}
.why-text .btn{margin-top:26px;padding:14px 34px;font-size:15px}
.why-art{flex:none;width:558px;height:250px;margin-left:18px;margin-top:50px;background:linear-gradient(180deg,#f7f9fa,#dfe9ec);border-bottom:2px solid #4a5a63}

/* alerts */
.alerts{height:349px;padding-top:60px}
.alerts h2{font-size:33px;font-weight:500;color:var(--link)}
.alert-list{display:flex;gap:72px;margin-top:20px;padding-left:15px}
.alert{width:420px;flex:none}
.alert h3{font-size:18px;font-weight:500;color:var(--link);line-height:1.35}
.alert p{font-size:14px;color:var(--muted);line-height:1.7;margin-top:6px}

/* footer */
.footer{height:352px;background:var(--navy);color:#fff}
.footer .wrap{display:flex;padding-top:66px;padding-left:22px}
.fcol{height:190px;padding-left:0}
.fcol + .fcol{border-left:1px solid rgba(255,255,255,.2);padding-left:30px}
.fcol.c1{width:190px}.fcol.c2{width:210px}.fcol.c3{width:240px}.fcol.c4{flex:1}
.fcol h4{font-size:19px;font-weight:500;letter-spacing:.3px}
.fcol ul{list-style:none;margin-top:12px}
.fcol li{font-size:13px;line-height:31px}
.contact li{display:flex;align-items:center;gap:10px}
.contact .indent{padding-left:24px}
.social{display:flex;gap:8px;margin-top:12px}
.social span{width:34px;height:34px;border:2px solid #fff;border-radius:50%}
.bottombar{height:70px;background:var(--navy-deep);color:rgba(255,255,255,.55);font-size:12px;text-align:center;line-height:70px}
</style>
</head>
<body>

<header class="hero">
  <div class="hero-photo" role="img" aria-label="Photo of colleagues reviewing financial charts and notes at a desk"></div>
  <div class="hero-shade"></div>
  <div class="wrap topbar">
    <div class="brand"><span class="brand-mark"></span><span>Harborline Ledger &amp; Advisory Partners</span></div>
    <ul class="nav">
      <li><a href="#">HOME</a></li>
      <li><a href="#">ABOUT US</a></li>
      <li><a href="#">SERVICES</a></li>
      <li><a href="#">FINANCIAL TOOLS</a></li>
      <li><a href="#">CONTACT US</a></li>
    </ul>
  </div>
  <svg class="arrow left" width="22" height="36" viewBox="0 0 22 36"><path d="M18 3 4 18l14 15" fill="none" stroke="#fff" stroke-width="4"/></svg>
  <svg class="arrow right" width="22" height="36" viewBox="0 0 22 36"><path d="M4 3l14 15L4 33" fill="none" stroke="#fff" stroke-width="4"/></svg>
  <div class="hero-copy">
    <h1 class="hero-title">ACCOUNTING &amp; TAX SERVICES</h1>
    <p class="hero-sub">ETIAM EST NUNC VENENATIS TRISTIQUE</p>
  </div>
</header>

<section class="services">
  <div class="wrap">
    <h2 class="section-title">What We Do</h2>
    <div class="rule"></div>
    <div class="cards">
      <div class="card">
        <svg class="card-icon" viewBox="0 0 100 100"><circle cx="50" cy="50" r="46" fill="#eef2f4"/><path d="M28 34h20v34H28zM52 34h20v34H52z" fill="none" stroke="#3f6f85" stroke-width="3"/></svg>
        <h3>Bookkeeping</h3>
        <p>Lorem ipsum dolor sit amet consectetuer adipiscing elit Nam cursus Morb</p>
        <a class="btn slate" href="#">READ MORE</a>
      </div>
      <div class="card">
        <svg class="card-icon" viewBox="0 0 100 100"><circle cx="50" cy="50" r="46" fill="#eef2f4"/><rect x="34" y="26" width="32" height="48" rx="3" fill="#4a94a6"/><rect x="39" y="31" width="22" height="9" fill="#fff"/><g fill="#fff"><rect x="39" y="45" width="6" height="6"/><rect x="47" y="45" width="6" height="6"/><rect x="55" y="45" width="6" height="6"/><rect x="39" y="55" width="6" height="6"/><rect x="47" y="55" width="6" height="6"/><rect x="55" y="55" width="6" height="6"/><rect x="39" y="65" width="6" height="5"/><rect x="47" y="65" width="14" height="5"/></g></svg>
        <h3>Accounting</h3>
        <p>Lorem ipsum dolor sit amet consectetuer adipiscing elit Nam cursus Morb</p>
        <a class="btn teal" href="#">READ MORE</a>
      </div>
      <div class="card">
        <svg class="card-icon" viewBox="0 0 100 100"><circle cx="50" cy="50" r="46" fill="#eef2f4"/><rect x="26" y="30" width="48" height="32" rx="2" fill="none" stroke="#1f5d7b" stroke-width="3"/><path d="M44 62v8h12v-8M40 72h20" fill="none" stroke="#1f5d7b" stroke-width="3"/><rect x="36" y="40" width="28" height="12" fill="none" stroke="#1f5d7b" stroke-width="2"/></svg>
        <h3>Tax Services</h3>
        <p>Lorem ipsum dolor sit amet consectetuer adipiscing elit Nam cursus Morb</p>
        <a class="btn navy" href="#">READ MORE</a>
      </div>
    </div>
  </div>
</section>

<section class="about">
  <div class="about-photo" role="img" aria-label="Teal-tinted photo of hands working with a calculator and documents"></div>
  <div class="about-copy">
    <h2>About Our Company</h2>
    <div class="rule"></div>
    <p>Welcome and thank you for visiting our website. At Harborline Ledger &amp; Advisory Partners, we have built our business so that it guarantees your success. In addition to providing you with a profile of our firm and the services we provide, this website has been designed to become a helpful resource tool to you, our valued clients and visitors.</p>
    <a class="btn ghost" href="#">READ MORE</a>
  </div>
</section>

<section class="why">
  <div class="wrap">
    <div class="why-text">
      <h2>Why We Are</h2>
      <p>Our firm endeavors to provide you with the highest quality of service and we hope that you find the information on this website useful.</p>
      <p>For any additional questions or comments please do not hesitate to contact us. We will get back to you as soon as possible as we pride ourselves on being proactive and responsive to our clients' inquiries and suggestions.</p>
      <a class="btn teal" href="#">READ MORE</a>
    </div>
    <div class="why-art" role="img" aria-label="Line illustration of an advisor presenting charts, calculators and finance icons"></div>
  </div>
</section>

<section class="alerts">
  <div class="wrap">
    <h2>Tax Alerts</h2>
    <div class="alert-list">
      <article class="alert">
        <h3>AB - 2017-18 Budget date announced</h3>
        <p>Alberta's President of the Treasury Board and Minister of Finance has announced that the province's 2017-18 Budget will be tabled on Thursday, March 16, 2017. The press release announcing ...</p>
      </article>
      <article class="alert">
        <h3>AB - Province issues updated carbon levy rates for 2017 and 2018</h3>
        <p>The province's new carbon levy came into effect as of January 1, 2017, and the Alberta Tax and Revenue Administration (TRA) has published the Carbon Levy Rates</p>
      </article>
    </div>
  </div>
</section>

<footer class="footer">
  <div class="wrap">
    <div class="fcol c1">
      <h4>COMPANY</h4>
      <ul><li>Home</li><li>About Us</li><li>Our Client</li><li>Why Us</li></ul>
    </div>
    <div class="fcol c2">
      <h4>SERVICES</h4>
      <ul><li>Bookkeeping</li><li>Accounting</li><li>Tax services</li></ul>
    </div>
    <div class="fcol c3">
      <h4>RESOURCES</h4>
      <ul><li>Support</li><li>Team</li><li>News &amp; Info</li><li>Contact Us</li></ul>
    </div>
    <div class="fcol c4">
      <h4>CONTACT US</h4>
      <ul class="contact">
        <li><svg width="14" height="18" viewBox="0 0 14 18"><path d="M7 1a6 6 0 0 0-6 6c0 4.5 6 10 6 10s6-5.5 6-10a6 6 0 0 0-6-6z" fill="#fff"/><circle cx="7" cy="7" r="2.3" fill="#0f3f5c"/></svg>48 Larchmere Row</li>
        <li class="indent">Edmonton, Alberta T5K 0Q1</li>
        <li><svg width="16" height="16" viewBox="0 0 16 16"><path d="M3 1h3l1.5 4-2 1.3a9 9 0 0 0 4.2 4.2L11 8.5l4 1.5v3a2 2 0 0 1-2 2A12 12 0 0 1 1 3a2 2 0 0 1 2-2z" fill="none" stroke="#fff" stroke-width="1.4"/></svg>(780) 555-0147</li>
        <li><svg width="16" height="12" viewBox="0 0 16 12"><rect x=".7" y=".7" width="14.6" height="10.6" fill="none" stroke="#fff" stroke-width="1.4"/><path d="M1 1l7 6 7-6" fill="none" stroke="#fff" stroke-width="1.4"/></svg>hello@harborlineledger.ca</li>
      </ul>
      <div class="social"><span></span><span></span><span></span><span></span></div>
    </div>
  </div>
</footer>
<div class="bottombar">© 2017 Company Name&nbsp; All right reserved</div>

</body>
</html>
```